Women sanitary pads, company name: Vela, need package design

We need 2 package designs for our women sanitary pads line. We want something relaxing, feminine and bold. The design can be the same for both packages. We just want the smaller one to have a white background since it is for day time and the bigger one to have a black background since it is for night time.

The name of the company is Vela = Boundlessly Golden, because many girls and women still ashamed of their menstrual period, we wanted to create something that would make them confortable with themselves and not to feel alone. The final design should communicate freedom, confidence, and being feminine.

Target Market(s)

Women from 13 years to 45 years.

Industry/Entity Type

It Company

Font styles to use
Serif
Sans Serif
Script

Colors

Designer to choose colors to be used in the design.

Requirements
Must have
• 4 harmonic feminine and relaxing colors.
• I uploaded 2 images . One is about the the flow chart and the other one is about the steps on how to use the pads. They do not have to be exactly the same. That is just an ideia.
• That is also the recycle symbol that we'd like to have.
Nice to have
• I'd like to see something simple, harmonic and eye-catching.
Should not have
• More than 4 colors.

```html
<!DOCTYPE html>
<html lang="en">
<head>
<meta charset="utf-8">
<title>Vela — Sanitary Pad Packaging</title>
<link rel="stylesheet" href="https://fonts.googleapis.com/css2?family=League+Spartan:wght@700&family=Lato:ital,wght@0,300;0,700;1,300&family=Kalam:wght@700&display=swap">
<style>
  :root {
    --brand-red: #e4032e;
    --ink: #1e1e1e;
    --label-grey: #9a9a9a;
    --board-grey: #f4f4f4;
    --day-blue: #00a0cc;
    --day-wash: #7fcde9;
    --day-sky: #d3ecf7;
    --night-black: #13050f;
    --night-deep: #2a0b28;
    --night-plum: #4b1550;
    --night-violet: #9a2f95;
    --night-glow: #b23cab;
    --skin: #f6d2b4;
    --white: #ffffff;
  }
  * { box-sizing: border-box; margin: 0; padding: 0; }
  html, body { width: 1200px; height: 1200px; overflow: hidden; background: var(--white); }
  .board { position: relative; width: 1200px; height: 1200px; font-family: "Lato", sans-serif; }

  .section-label {
    position: absolute; left: 85px;
    font-family: "Lato", sans-serif; font-weight: 300;
    font-size: 19px; letter-spacing: 0.5px; color: var(--label-grey);
  }
  .band-front { position: absolute; left: 0; top: 290px; width: 1200px; height: 464px; background: var(--board-grey); }

  .brand-lockup { position: absolute; left: 0; top: 62px; width: 1200px; text-align: center; }
  .brand-name {
    font-family: "League Spartan", sans-serif; font-weight: 700;
    font-size: 150px; line-height: 0.9; color: var(--brand-red); letter-spacing: -2px;
  }
  .brand-tagline {
    font-family: "Kalam", cursive; font-weight: 700;
    font-size: 40px; line-height: 1; color: var(--ink); margin-top: 6px;
  }

  .pack { position: absolute; overflow: hidden; container-type: inline-size; }
  .pack--preview { border-radius: 16px; box-shadow: 0 8px 16px rgba(0,0,0,0.10); }
  .pack--day { background: var(--white); }
  .pack--night { background: var(--night-black); }

  /* illustration area: soft wash in the artwork's main tones */
  .pack__art { position: absolute; top: 0; height: 100%; }
  .pack--day .pack__art {
    left: 38%; width: 62%;
    background:
      radial-gradient(ellipse 26% 22% at 50% 30%, rgba(246,210,180,0.85) 0%, rgba(246,210,180,0) 100%),
      radial-gradient(ellipse 30% 34% at 52% 62%, rgba(255,255,255,0.95) 0%, rgba(255,255,255,0) 100%),
      radial-gradient(ellipse 48% 55% at 50% 45%, var(--day-wash) 0%, var(--day-sky) 55%, rgba(211,236,247,0) 100%),
      radial-gradient(ellipse 70% 60% at 70% 20%, rgba(211,236,247,0.7) 0%, rgba(211,236,247,0) 100%);
  }
  .pack--night .pack__art {
    left: 30%; width: 70%;
    background:
      radial-gradient(ellipse 24% 20% at 62% 62%, rgba(246,210,180,0.9) 0%, rgba(246,210,180,0) 100%),
      radial-gradient(ellipse 40% 16% at 70% 86%, rgba(255,255,255,0.9) 0%, rgba(255,255,255,0) 100%),
      radial-gradient(ellipse 50% 50% at 62% 66%, var(--night-glow) 0%, var(--night-violet) 35%, rgba(75,21,80,0) 100%),
      radial-gradient(ellipse 80% 60% at 80% 15%, var(--night-plum) 0%, var(--night-deep) 50%, rgba(19,5,15,0) 100%);
    -webkit-mask-image: linear-gradient(90deg, transparent 0%, #000 25%);
            mask-image: linear-gradient(90deg, transparent 0%, #000 25%);
  }

  .pack__name {
    position: absolute; left: 6%; top: 13%;
    font-family: "League Spartan", sans-serif; font-weight: 700;
    font-size: 13.5cqw; line-height: 0.9; letter-spacing: -0.3cqw;
  }
  .pack--day .pack__name { color: var(--brand-red); }
  .pack--night .pack__name { color: var(--white); }
  .pack__tagline {
    position: absolute; left: 6.5%; top: 27%;
    font-family: "Kalam", cursive; font-weight: 700; font-size: 3.6cqw; line-height: 1;
  }
  .pack--day .pack__tagline { color: var(--ink); }
  .pack--night .pack__tagline { color: var(--white); }

  .pack__mood {
    position: absolute; left: 5%; top: 47%;
    font-family: "Kalam", cursive; font-weight: 700; font-size: 8.6cqw; line-height: 1;
  }
  .pack--day .pack__mood { color: var(--day-blue); }
  .pack--night .pack__mood { color: var(--night-violet); }

  .pack__base { position: absolute; left: 0; bottom: 0; width: 100%; height: 30%; }

  .pack__count { position: absolute; left: 6%; bottom: 9%; display: flex; align-items: flex-end; color: var(--white); }
  .pack__count-number { font-family: "Lato", sans-serif; font-weight: 700; font-size: 12cqw; line-height: 0.8; }
  .pack__count-text { margin-left: 1.2cqw; }
  .pack__count-label { font-style: italic; font-weight: 300; font-size: 4.3cqw; line-height: 1.1; }
  .pack__drops { display: flex; gap: 0.3cqw; margin-top: 0.4cqw; }
  .pack__drops svg { width: 3.2cqw; height: 4.2cqw; }
</style>
</head>
<body>
<main class="board">

  <p class="section-label" style="top:58px;">LOGO</p>
  <header class="brand-lockup">
    <div class="brand-name">Vela</div>
    <div class="brand-tagline">Boundlessly Golden!</div>
  </header>

  <div class="band-front"></div>
  <p class="section-label" style="top:315px;">FRONT DESIGN</p>

  <!-- Day pack front -->
  <section class="pack pack--day" style="left:150px; top:360px; width:412px; height:330px;">
    <div class="pack__art" role="img" aria-label="Illustration of a cheerful girl in a white dress running, on a soft watercolour sky-blue wash with light doodles and clouds"></div>
    <div class="pack__name">Vela</div>
    <div class="pack__tagline">Boundlessly Golden!</div>
    <div class="pack__mood">Happy Day</div>
    <svg class="pack__base" viewBox="0 0 100 30" preserveAspectRatio="none"><path d="M0 2 Q42 -2 74 30 L0 30 Z" fill="var(--day-blue)"/></svg>
    <div class="pack__count">
      <span class="pack__count-number">2</span>
      <div class="pack__count-text">
        <div class="pack__count-label">sanitary pads</div>
        <div class="pack__drops">
          <svg viewBox="0 0 10 13"><path d="M5 1 C7 5 9 7 9 9 A4 4 0 0 1 1 9 C1 7 3 5 5 1 Z" fill="none" stroke="var(--white)" stroke-width="1.3"/></svg>
          <svg viewBox="0 0 10 13"><path d="M5 1 C7 5 9 7 9 9 A4 4 0 0 1 1 9 C1 7 3 5 5 1 Z" fill="none" stroke="var(--white)" stroke-width="1.3"/></svg>
          <svg viewBox="0 0 10 13"><path d="M5 1 C7 5 9 7 9 9 A4 4 0 0 1 1 9 C1 7 3 5 5 1 Z" fill="none" stroke="var(--white)" stroke-width="1.3"/></svg>
        </div>
      </div>
    </div>
  </section>

  <!-- Night pack front -->
  <section class="pack pack--night" style="left:614px; top:341px; width:436px; height:350px;">
    <svg class="pack__base" viewBox="0 0 100 30" preserveAspectRatio="none"><path d="M0 4 Q35 -3 70 3 Q88 6 100 12 L100 30 L0 30 Z" fill="var(--night-plum)"/></svg>
    <div class="pack__art" role="img" aria-label="Illustration of a girl sleeping peacefully on a white pillow, under a violet glow with a starry night pattern"></div>
    <div class="pack__name">Vela</div>
    <div class="pack__tagline">Boundlessly Golden!</div>
    <div class="pack__mood">Good Night</div>
    <div class="pack__count">
      <span class="pack__count-number">2</span>
      <div class="pack__count-text">
        <div class="pack__count-label">sanitary pads</div>
        <div class="pack__drops">
          <svg viewBox="0 0 10 13"><path d="M5 1 C7 5 9 7 9 9 A4 4 0 0 1 1 9 C1 7 3 5 5 1 Z" fill="none" stroke="var(--white)" stroke-width="1.3"/></svg>
          <svg viewBox="0 0 10 13"><path d="M5 1 C7 5 9 7 9 9 A4 4 0 0 1 1 9 C1 7 3 5 5 1 Z" fill="none" stroke="var(--white)" stroke-width="1.3"/></svg>
          <svg viewBox="0 0 10 13"><path d="M5 1 C7 5 9 7 9 9 A4 4 0 0 1 1 9 C1 7 3 5 5 1 Z" fill="none" stroke="var(--white)" stroke-width="1.3"/></svg>
          <svg viewBox="0 0 10 13"><path d="M5 1 C7 5 9 7 9 9 A4 4 0 0 1 1 9 C1 7 3 5 5 1 Z" fill="none" stroke="var(--white)" stroke-width="1.3"/></svg>
          <svg viewBox="0 0 10 13"><path d="M5 1 C7 5 9 7 9 9 A4 4 0 0 1 1 9 C1 7 3 5 5 1 Z" fill="none" stroke="var(--white)" stroke-width="1.3"/></svg>
        </div>
      </div>
    </div>
  </section>

  <p class="section-label" style="top:793px;">PREVIEW</p>

  <!-- Day pack preview -->
  <section class="pack pack--day pack--preview" style="left:164px; top:842px; width:384px; height:294px;">
    <div class="pack__art" role="img" aria-label="Illustration of a cheerful girl in a white dress running, on a soft watercolour sky-blue wash"></div>
    <div class="pack__name">Vela</div>
    <div class="pack__tagline">Boundlessly Golden!</div>
    <div class="pack__mood">Happy Day</div>
    <svg class="pack__base" viewBox="0 0 100 30" preserveAspectRatio="none"><path d="M0 2 Q42 -2 74 30 L0 30 Z" fill="var(--day-blue)"/></svg>
    <div class="pack__count">
      <span class="pack__count-number">2</span>
      <div class="pack__count-text">
        <div class="pack__count-label">sanitary pads</div>
        <div class="pack__drops">
          <svg viewBox="0 0 10 13"><path d="M5 1 C7 5 9 7 9 9 A4 4 0 0 1 1 9 C1 7 3 5 5 1 Z" fill="none" stroke="var(--white)" stroke-width="1.3"/></svg>
          <svg viewBox="0 0 10 13"><path d="M5 1 C7 5 9 7 9 9 A4 4 0 0 1 1 9 C1 7 3 5 5 1 Z" fill="none" stroke="var(--white)" stroke-width="1.3"/></svg>
          <svg viewBox="0 0 10 13"><path d="M5 1 C7 5 9 7 9 9 A4 4 0 0 1 1 9 C1 7 3 5 5 1 Z" fill="none" stroke="var(--white)" stroke-width="1.3"/></svg>
        </div>
      </div>
    </div>
  </section>

  <!-- Night pack preview -->
  <section class="pack pack--night pack--preview" style="left:632px; top:826px; width:406px; height:310px;">
    <svg class="pack__base" viewBox="0 0 100 30" preserveAspectRatio="none"><path d="M0 4 Q35 -3 70 3 Q88 6 100 12 L100 30 L0 30 Z" fill="var(--night-plum)"/></svg>
    <div class="pack__art" role="img" aria-label="Illustration of a girl sleeping on a white pillow under a violet glow with a starry night pattern"></div>
    <div class="pack__name">Vela</div>
    <div class="pack__tagline">Boundlessly Golden!</div>
    <div class="pack__mood">Good Night</div>
    <div class="pack__count">
      <span class="pack__count-number">2</span>
      <div class="pack__count-text">
        <div class="pack__count-label">sanitary pads</div>
        <div class="pack__drops">
          <svg viewBox="0 0 10 13"><path d="M5 1 C7 5 9 7 9 9 A4 4 0 0 1 1 9 C1 7 3 5 5 1 Z" fill="none" stroke="var(--white)" stroke-width="1.3"/></svg>
          <svg viewBox="0 0 10 13"><path d="M5 1 C7 5 9 7 9 9 A4 4 0 0 1 1 9 C1 7 3 5 5 1 Z" fill="none" stroke="var(--white)" stroke-width="1.3"/></svg>
          <svg viewBox="0 0 10 13"><path d="M5 1 C7 5 9 7 9 9 A4 4 0 0 1 1 9 C1 7 3 5 5 1 Z" fill="none" stroke="var(--white)" stroke-width="1.3"/></svg>
          <svg viewBox="0 0 10 13"><path d="M5 1 C7 5 9 7 9 9 A4 4 0 0 1 1 9 C1 7 3 5 5 1 Z" fill="none" stroke="var(--white)" stroke-width="1.3"/></svg>
          <svg viewBox="0 0 10 13"><path d="M5 1 C7 5 9 7 9 9 A4 4 0 0 1 1 9 C1 7 3 5 5 1 Z" fill="none" stroke="var(--white)" stroke-width="1.3"/></svg>
        </div>
      </div>
    </div>
  </section>

</main>
</body>
</html>
```